We are looking for a simple design that would be uplifting for
upscale drug addicts

MERIDIAN CIRCLE

PLEASE SEE THE LINK FOR TAG LINE AND CONTENT

thank you.

here is all the actual info we need and we want something like this...

http://assets.qlm.brivostore.com/rest/items/7c2910e5b337de81f94a02bd57e644163ab9fe0a6712?uid=bd31c9e2f7a04c18b6e0d44721fa93c5%2fdrafts&expires=1408211537&signature=kTp4WmQxNvLzHa8YbEoRcJsGf2B%3d

The shape and colors don't have to be like what I posted it is only an example.

Target Market(s)

Wall Street, internet and creative types, men, early 30's,
upwardly mobile, drug addicts

current site

bkltornavel.com

now launching new name Meridian Circle

Industry/Entity Type

Drug

Requirements
Must have
• upscale look, great font
Should not have
• a corporate look but should not look like a clinic.

```html
<!DOCTYPE html>
<html lang="en">
<head>
<meta charset="utf-8">
<title>Meridian Circle – Business Card</title>
<link href="https://fonts.googleapis.com/css2?family=Roboto:wght@400;500&display=swap" rel="stylesheet">
<style>
  :root {
    --brand-blue: #0891c8;
    --card-white: #ffffff;
    --page-bg: #ececec;
    --rule-grey: #8a8a8a;
  }
  * { margin: 0; padding: 0; box-sizing: border-box; }
  html, body { width: 1200px; height: 900px; overflow: hidden; }
  body {
    background: var(--page-bg);
    font-family: "Roboto", Arial, sans-serif;
    position: relative;
  }
  .business-card {
    position: absolute;
    left: 80px; top: 161px;
    width: 1040px; height: 578px;
    background: var(--card-white);
    box-shadow: 0 18px 30px -14px rgba(0,0,0,0.35);
    overflow: hidden;
  }
  .card-header { position: absolute; left: 0; top: 0; width: 1040px; height: 110px; }
  .brand-name {
    position: absolute; left: 33px; top: 20px;
    color: var(--card-white);
    font-weight: 400; font-size: 52px; letter-spacing: -1px;
    line-height: 1;
  }
  .tagline {
    position: absolute; left: 672px; top: 34px; width: 360px;
    color: var(--brand-blue);
    font-size: 17px; line-height: 23px;
  }
  .name-rule {
    position: absolute; left: 16px; top: 310px;
    width: 472px; height: 4px; background: var(--brand-blue);
  }
  .person-name {
    position: absolute; right: 33px; top: 272px;
    color: var(--brand-blue);
    font-weight: 500; font-size: 52px; letter-spacing: -1px; line-height: 1;
  }
  .person-title {
    position: absolute; right: 43px; top: 340px;
    color: var(--brand-blue);
    font-size: 29px; line-height: 1;
  }
  .contact-item {
    position: absolute; top: 510px;
    display: flex; align-items: flex-start; gap: 14px;
    color: var(--brand-blue); font-size: 20px; line-height: 23px;
  }
  .contact-item svg { flex: none; width: 38px; height: 38px; margin-top: 4px; }
  .contact-address { left: 52px; }
  .contact-phone { left: 370px; }
  .contact-email { left: 618px; }
  .contact-email svg { margin-top: -6px; }
  .contact-address address { font-style: normal; }
  .footer-band {
    position: absolute; left: 0; bottom: 0;
    width: 100%; height: 8px; background: var(--brand-blue);
  }
</style>
</head>
<body>
  <section class="business-card" aria-label="Meridian Circle business card">
    <svg class="card-header" viewBox="0 0 1040 110" aria-hidden="true">
      <polygon points="0,0 680,0 594,106 0,106" fill="var(--brand-blue)"/>
      <line x1="0" y1="98" x2="601" y2="98" stroke="#ffffff" stroke-width="2" stroke-dasharray="9 7"/>
      <line x1="601" y1="98" x2="1040" y2="98" stroke="var(--rule-grey)" stroke-width="2" stroke-dasharray="9 7"/>
    </svg>
    <div class="brand-name">MERIDIAN CIRCLE</div>
    <p class="tagline">We walk beside you every step of the way toward lasting recovery</p>

    <div class="name-rule"></div>
    <h1 class="person-name">Daniel Varo, CASAC</h1>
    <p class="person-title">Program Coordinator</p>

    <div class="contact-item contact-address">
      <svg viewBox="0 0 38 38" aria-hidden="true">
        <circle cx="19" cy="19" r="17" fill="none" stroke="var(--brand-blue)" stroke-width="2"/>
        <polygon points="9,18 28,10 21,29 18,21" fill="none" stroke="var(--brand-blue)" stroke-width="2" stroke-linejoin="round"/>
      </svg>
      <address>418 W. 52nd St. Suite 302<br>New York, NY 10019</address>
    </div>

    <div class="contact-item contact-phone">
      <svg viewBox="0 0 38 38" aria-hidden="true">
        <circle cx="19" cy="19" r="17" fill="none" stroke="var(--brand-blue)" stroke-width="2"/>
        <path d="M12 10 L16 9 L18 15 L15 17 Q18 23 22 25 L24 22 L30 24 L29 28 Q20 30 14 22 Q10 16 12 10 Z" fill="none" stroke="var(--brand-blue)" stroke-width="2" stroke-linejoin="round"/>
      </svg>
      <div>212.555.0148<br>212.555.0149</div>
    </div>

    <div class="contact-item contact-email">
      <svg viewBox="0 0 38 38" aria-hidden="true">
        <circle cx="19" cy="19" r="17" fill="none" stroke="var(--brand-blue)" stroke-width="2"/>
        <polyline points="9,26 9,13 19,21 29,13 29,26" fill="none" stroke="var(--brand-blue)" stroke-width="2" stroke-linejoin="round"/>
      </svg>
      <div>counselor@meridiancirclenyc.com</div>
    </div>

    <div class="footer-band"></div>
  </section>
</body>
</html>
```